The Quiet Hour Safeguard Handbook

A book cover. The book will be marketed as a promotional item for financial advisors, financial planners, independent insurance agents, bankers, and any professional who views their role as guardian of their clients assets and helping them manage risk.

```html
<!DOCTYPE html>
<html lang="en">
<head>
<meta charset="UTF-8">
<title>The Quiet Hour Safeguard Handbook</title>
<link href="https://fonts.googleapis.com/css2?family=Arimo:ital,wght@0,400;0,700;1,400&display=swap" rel="stylesheet">
<style>
  :root {
    --page: #ffffff;
    --navy: #37557a;
    --gold: #e8c22e;
    --white: #ffffff;
  }
  html, body {
    margin: 0;
    padding: 0;
    width: 927px;
    height: 1200px;
    overflow: hidden;
    background: var(--page);
  }
  .cover {
    position: relative;
    width: 927px;
    height: 1200px;
    font-family: "Arimo", Arial, sans-serif;
  }
  .cover-panel {
    position: absolute;
    left: 51px;
    top: 54px;
    width: 818px;
    height: 1025px;
    background: var(--navy);
  }
  .top-rule {
    position: absolute;
    left: 0;
    top: 25px;
    width: 100%;
    height: 3px;
    background: var(--gold);
  }
  .title {
    position: absolute;
    left: 0;
    top: 318px;
    width: 100%;
    margin: 0;
    text-align: center;
    color: var(--white);
    font-weight: 700;
    font-size: 55px;
    line-height: 63px;
    letter-spacing: 0.2px;
  }
  .title span { display: block; }
  .subtitle {
    position: absolute;
    left: 0;
    top: 448px;
    width: 100%;
    margin: 0;
    text-align: center;
    color: var(--gold);
    font-style: italic;
    font-weight: 400;
    font-size: 18.5px;
    line-height: 22px;
  }
  .divider {
    position: absolute;
    left: 278px;
    top: 488px;
    width: 264px;
    height: 14px;
  }
  .tagline {
    position: absolute;
    left: 0;
    top: 529px;
    width: 100%;
    margin: 0;
    text-align: center;
    color: var(--white);
    font-weight: 700;
    font-size: 16px;
    line-height: 25px;
    text-transform: uppercase;
  }
</style>
</head>
<body>
  <main class="cover">
    <section class="cover-panel">
      <div class="top-rule"></div>
      <h1 class="title">
        <span>The Quiet Hour</span>
        <span>Safeguard Handbook</span>
      </h1>
      <p class="subtitle">Protect Yourself and Your Family in the AI Age</p>
      <svg class="divider" viewBox="0 0 264 14" aria-hidden="true">
        <line x1="0" y1="7" x2="115" y2="7" stroke="var(--gold)" stroke-width="1.2"/>
        <rect x="127.5" y="2.5" width="9" height="9" fill="var(--gold)" transform="rotate(45 132 7)"/>
        <line x1="149" y1="7" x2="264" y2="7" stroke="var(--gold)" stroke-width="1.2"/>
      </svg>
      <p class="tagline">It’s better to have it and not need it<br>than need it and not have it.</p>
    </section>
  </main>
</body>
</html>
```